Bright Vessel, Accelerator for Healthcare Startups, Grand Opening

Bright Vessel is an accelerator for healthcare startup businesses located in North Chicago, Illinois, USA. On July 16th, 4:30 - 6:30 pm, we are having a Grand Opening of our new location, which is at 2417 Calloway, North Chicago, IL. There will be many local dignitaries in attendance, but most importantly we will be unveiling the healthcare startup businesses that will be in our next cohort. We also have four sponsors, logos attached. Here's our website: http://brightvessel.example/

Target Market(s)

Investors, Healthcare Professionals, Politicians, Dignitaries

Industry/Entity Type

Healthcare

Requirements
Must have
• Logo, Date, Time, Location, Sponsors.
Nice to have
• Extremely elegant, professional design.
Should not have
• This is NOT and opening for retail. This is very professional.

```html
<!DOCTYPE html>
<html lang="en">
<head>
<meta charset="utf-8">
<title>Bright Vessel — Grand Opening</title>
<link rel="stylesheet" href="https://fonts.googleapis.com/css2?family=Oswald:wght@500&family=Tinos:wght@700&family=Marcellus&display=swap">
<style>
  :root {
    --backdrop: #ece8e2;
    --card-black: #111111;
    --card-charcoal: #2a2a2a;
    --ink-white: #ffffff;
    --ink-soft: #e9e9e9;
    --band-white: #ffffff;
    --ink-dark: #3a2a24;
    --ornament-tone: #8a8a8a;
  }
  * { margin: 0; padding: 0; box-sizing: border-box; }
  html, body { width: 1200px; height: 1000px; overflow: hidden; background: var(--backdrop); }
  .canvas { position: relative; width: 1200px; height: 1000px; }

  .flyer {
    position: absolute; left: 300px; top: 90px; width: 600px; height: 820px;
    background: var(--card-black);
    box-shadow: 0 6px 24px rgba(0,0,0,.25);
    overflow: hidden;
  }
  .flyer__pattern {
    position: absolute; inset: 0 0 120px 0;
    background: radial-gradient(ellipse at 50% 45%, var(--card-charcoal) 0%, var(--card-black) 75%);
  }
  .ornament {
    position: absolute; left: 50%; transform: translateX(-50%);
    background: var(--ornament-tone); opacity: .35; border-radius: 40px;
  }
  .ornament--top { top: 62px; width: 330px; height: 50px; }
  .ornament--bottom { top: 598px; width: 110px; height: 30px; }

  .flyer__content { position: relative; text-align: center; color: var(--ink-white); }
  .brand {
    margin-top: 118px;
    font-family: "Oswald", sans-serif; font-weight: 500;
    font-size: 54px; letter-spacing: 1px; line-height: 1;
    text-transform: uppercase; color: var(--ink-white);
  }
  .event-date { margin-top: 22px; font-family: "Tinos", serif; font-weight: 700; font-size: 23px; }
  .event-time { margin-top: 2px; font-family: "Tinos", serif; font-weight: 700; font-size: 13px; }
  .event-place { margin-top: 2px; font-family: "Tinos", serif; font-weight: 700; font-size: 19px; }
  .blurb {
    margin: 26px auto 0; width: 500px;
    font-family: "Marcellus", serif; font-size: 19.5px; line-height: 1.42;
    text-align: justify; text-align-last: center; color: var(--ink-soft);
    hyphens: auto;
  }
  .sponsor-label {
    position: absolute; top: 640px; width: 100%; text-align: center;
    font-family: "Tinos", serif; font-size: 17px; letter-spacing: 1px; color: var(--ink-white);
  }
  .sponsors {
    position: absolute; left: 0; bottom: 0; width: 100%; height: 120px;
    background: var(--band-white);
    display: flex; align-items: center; justify-content: space-around; padding: 0 24px;
  }
  .sponsor {
    display: flex; align-items: center; gap: 8px;
    font-family: "Marcellus", serif; font-size: 17px; color: var(--ink-dark);
  }
  .sponsor__mark { width: 14px; height: 14px; border-radius: 50%; background: var(--ink-dark); }
</style>
</head>
<body>
<main class="canvas">
  <article class="flyer">
    <div class="flyer__pattern" role="img" aria-label="Dark damask swirl pattern background"></div>
    <div class="ornament ornament--top" role="img" aria-label="Decorative flourish"></div>
    <div class="ornament ornament--bottom" role="img" aria-label="Small decorative flourish"></div>

    <div class="flyer__content">
      <h1 class="brand">Bright Vessel</h1>
      <p class="event-date">16th July 2015</p>
      <p class="event-time">4:30pm - 6:30 pm</p>
      <p class="event-place">North Chicago, Illionis, USA</p>
      <p class="blurb">Nestled at the doorstep of healthcare giants, including Ardent Labs, Corvane, Meridel, Halvern, Pellworth, Lakeshore Valley Health Network, Sorrento Bio, and Greystone Pharmacy, Bright Vessel is an accelerator, providing healthcare startups access to customers, mentors, investors, seed funding and co-working space to facilitate innovation and growth.</p>
    </div>

    <p class="sponsor-label">SPONSORED BY</p>
    <footer class="sponsors">
      <span class="sponsor">Hopwright</span>
      <span class="sponsor"><span class="sponsor__mark"></span>roastandvessel.example</span>
      <span class="sponsor">Candor Sweets</span>
      <span class="sponsor">Ember Kitchen</span>
    </footer>
  </article>
</main>
</body>
</html>
```